Luxurious Rustic Cottage Accommodation brochure design

I would like a trifold brochure design to continue the theme I already have established on my website www.atbellcroft.com.au The basic theme uses the logo from the website, it is called "At Bellcroft" B & B Private Cottages and has black background with use of gold for borders and highlights. The accommodation is in the hinterland region of the Sunshine Coast, Queensland, Australia. I have 4 separate private cottages which I would like to include information & pictures about each as per details on the website mentioned. Features to highlight include ocean views, log fires, spa baths, romance, nature. Accommodation is suitable for couples, family, small group or wedding party, special occasion getways. Package inclusions to be highlighted are breakfast hamper, complimentary chocolates & champagne, pamper products, optional inclusions are cheese platter, relaxation massage. I would like location to be included by way of a map, contact details (website, email & mobile phone) to also be included.
There are pictures on the website which I can provide high resolution for brochure printing as required. Some more images have been uploaded for optional use.
Accommodation

```html
<!DOCTYPE html>
<html lang="en">
<head>
<meta charset="utf-8">
<title>At Bellcroft – Trifold Brochure</title>
<link href="https://fonts.googleapis.com/css2?family=PT+Sans:ital,wght@0,400;0,700;1,700&display=swap" rel="stylesheet">
<style>
  :root{
    --stage:#3a3d42;
    --paper:#ffffff;
    --ink:#1a1a1a;
    --black:#0b0b0b;
    --gold:#b88f3c;
    --grey:#8d8f93;
    --white:#ffffff;
  }
  *{box-sizing:border-box;margin:0;padding:0}
  html,body{width:1200px;height:982px;overflow:hidden}
  body{
    background:radial-gradient(ellipse at 50% 35%,#5a5e64 0%,var(--stage) 70%);
    font-family:"PT Sans",Arial,sans-serif;color:var(--ink);position:relative;
  }
  .brochure{position:absolute;left:45px;top:111px;width:1110px;height:760px;background:var(--paper);box-shadow:0 20px 50px rgba(0,0,0,.45);overflow:hidden}
  .panel{position:absolute;top:0;width:370px;height:760px;overflow:hidden}
  .panel--left{left:0}
  .panel--middle{left:370px;border-left:1px solid #e6e6e6}
  .panel--right{left:740px;border-left:1px solid #e6e6e6}
  .photo{position:absolute}
  .swoosh{position:absolute;left:0;width:100%}

  /* left panel */
  .photo--spa-strip{left:0;top:0;width:370px;height:70px;background:linear-gradient(90deg,#cfd6d2,#eef1ef 60%,#b9c2bc)}
  .photo--garden-sign{left:0;top:490px;width:370px;height:270px;background:linear-gradient(160deg,#5f7d3d 0%,#9a6a3a 35%,#6b2f5a 75%,#3f1d38 100%)}
  .activities{position:absolute;left:28px;top:98px;width:320px;font-size:13px;line-height:1.27}
  .activities h3{font-style:italic;font-weight:700;font-size:15px;color:var(--ink);margin-bottom:2px}
  .activities .item{color:var(--gold);font-weight:700;font-style:italic}
  .activities .sub{font-size:11px;color:#444;padding-left:6px}
  .activities .row{display:flex;justify-content:space-between;align-items:baseline}
  .activities h3.venture{margin-top:5px}

  /* middle panel */
  .photo--spa{left:0;top:0;width:370px;height:280px;background:linear-gradient(150deg,#e9ecea 0%,#ffffff 40%,#c8d3c6 70%,#7f9a78 100%)}
  .brand-mark{position:absolute;left:0;top:300px;width:370px;display:flex;justify-content:center;align-items:center;gap:10px}
  .brand-mark .dot{width:22px;height:22px;border-radius:50%;background:var(--gold)}
  .brand-mark span{font-size:26px;font-weight:700;color:var(--ink)}
  .map{position:absolute;left:40px;top:355px;width:290px;height:205px;border:6px solid var(--gold);background:linear-gradient(135deg,#e7eadf,#f4f2ea 50%,#dfe6d6)}
  .contact{position:absolute;left:0;top:585px;width:370px;text-align:center;line-height:1.35}
  .contact .names{font-weight:700;font-size:21px}
  .contact .phone{font-size:21px}
  .contact .phone b{font-weight:700}
  .contact .email,.contact .web{font-size:15px}
  .contact .email b,.contact .web b{font-weight:700}
  .contact .address{font-size:15px}

  /* right panel */
  .photo--spa-edge{left:0;top:0;width:370px;height:130px;background:linear-gradient(120deg,#dfe5dc,#9fb39a 70%,#6c8064)}
  .logo-block{position:absolute;left:0;top:130px;width:370px;height:205px;background:var(--black);color:var(--white);text-align:center}
  .logo-block .brand-row{display:flex;align-items:center;justify-content:center;gap:12px;margin-top:36px}
  .logo-block .brand-row .dot{width:26px;height:26px;border-radius:50%;background:var(--gold)}
  .logo-block .brand-name{font-size:44px;font-weight:400;letter-spacing:3px}
  .logo-block .brand-sub{width:230px;margin:2px auto 0;display:flex;justify-content:space-between;font-size:12px;letter-spacing:1px}
  .logo-block .tagline{font-size:17px;margin-top:22px;line-height:1.25}
  .rule--gold{position:absolute;left:0;top:335px;width:370px;height:5px;background:var(--gold)}
  .photo--cabin{left:0;top:340px;width:370px;height:260px;background:linear-gradient(160deg,#a9c6e0 0%,#7b5a45 35%,#5f7a3f 65%,#8fa85c 100%)}
  .features{position:absolute;left:0;top:640px;width:370px;text-align:center;color:var(--white);font-weight:700;font-size:17px;line-height:1.35}
  .book{position:absolute;left:0;top:718px;width:370px;text-align:center;color:var(--white);font-size:22px}
  .book b{font-weight:700;font-size:27px}
</style>
</head>
<body>
<main class="brochure">

  <section class="panel panel--left">
    <div class="photo photo--spa-strip" role="img" aria-label="Photo of a bubble-filled spa bath with a view"></div>
    <svg class="swoosh" style="top:60px" width="370" height="40" viewBox="0 0 370 40" aria-hidden="true">
      <path d="M0 10 L370 10 L370 40 Q200 18 0 24 Z" fill="var(--gold)"/>
    </svg>
    <div class="activities">
      <h3>In House Activities</h3>
      <div class="item">Binoculars For Bird Watching,</div>
      <div class="item">Exploring The Coastline &amp; Passing Ships</div>
      <div class="item">Dvd, Cd &amp; Games Library</div>
      <div class="item">Weekend Newspapers</div>
      <div class="item">Massage</div>
      <div class="row sub"><span>• Temple Massage</span><span>• Ripple Massage</span></div>
      <h3 class="venture">Venture Out</h3>
      <div class="item">Great Walks</div>
      <div class="item">Picnic Areas</div>
      <div class="item">Shops</div>
      <div class="sub">• Maleny</div>
      <div class="row"><span class="item">Restaurants</span><span class="sub">• Montville</span></div>
      <div class="sub">• Maleny</div>
      <div class="row"><span class="item">Wineries</span><span class="sub">• Montville</span></div>
      <div class="item">Cheese Tasting</div>
      <div class="row sub"><span>• Valley Cheese</span><span>• Ridgeline Country Foods</span></div>
    </div>
    <svg class="swoosh" style="top:440px" width="370" height="60" viewBox="0 0 370 60" aria-hidden="true">
      <path d="M0 10 Q180 30 370 18 L370 60 L0 60 Z" fill="var(--black)"/>
      <path d="M0 22 Q180 40 370 30 L370 60 L0 60 Z" fill="var(--grey)"/>
    </svg>
    <div class="photo photo--garden-sign" role="img" aria-label="Photo of a carved timber cottage name sign among purple garden foliage"></div>
  </section>

  <section class="panel panel--middle">
    <div class="photo photo--spa" role="img" aria-label="Photo of a bubble spa bath with champagne glasses overlooking the hinterland"></div>
    <svg class="swoosh" style="top:220px" width="370" height="70" viewBox="0 0 370 70" aria-hidden="true">
      <path d="M0 0 Q160 40 370 30 L370 70 L0 70 Z" fill="var(--paper)"/>
      <path d="M0 0 Q160 40 370 30 L370 40 Q160 52 0 14 Z" fill="var(--gold)"/>
    </svg>
    <div class="brand-mark"><div class="dot"></div><span>At Bellcroft</span></div>
    <div class="map" role="img" aria-label="Road map showing the cottage location near Montville"></div>
    <div class="contact">
      <div class="names">Mark &amp; Tessa Holloway</div>
      <div class="phone">Contact Us : <b>0400 555 218</b></div>
      <div class="email">Email us : <b>tessa@atbellcroft.com.au</b></div>
      <div class="web">www.<b>tessa@atbellcroft.com.au</b></div>
      <div class="address">Bellcroft Lane 27 Ridgeview Road<br>Montville&nbsp; QLD&nbsp; 4560</div>
    </div>
  </section>

  <section class="panel panel--right">
    <div class="photo photo--spa-edge" role="img" aria-label="Photo of the spa deck with garden view"></div>
    <div class="logo-block">
      <div class="brand-row"><div class="dot"></div><span class="brand-name">Bellcroft</span></div>
      <div class="brand-sub"><span>bed &amp; breakfast</span><span>private cottages</span></div>
      <div class="tagline">Luxurious Rustic Cabin &amp; Lodge<br>Accommodation in Montville, Queensland</div>
    </div>
    <div class="rule--gold"></div>
    <div class="photo photo--cabin" role="img" aria-label="Photo of a rustic cabin with tiled roof surrounded by garden"></div>
    <svg class="swoosh" style="top:570px" width="370" height="190" viewBox="0 0 370 190" aria-hidden="true">
      <path d="M0 20 Q200 -5 370 40 L370 190 L0 190 Z" fill="var(--black)"/>
      <path d="M0 30 Q200 6 370 50 L370 190 L0 190 Z" fill="var(--grey)"/>
      <path d="M0 40 Q200 18 370 60 L370 190 L0 190 Z" fill="var(--gold)"/>
    </svg>
    <div class="features">
      Complimentary Shuttle<br>Wireless Internet<br>BBQ/Picnic Hampers
    </div>
    <div class="book">Book Now : <b>0400 555 218</b></div>
  </section>

</main>
</body>
</html>
```